Need a logo/cover design for my book Golden Handshake Hours: How We Turned Coffee Chats Into Fortunes With Friends Worth Keeping

Over the years I've worked in chambers of commerce and at high-profile country clubs and have had access to very successful people and the companies they work for or launch. Through meeting people, learning from them, applying what I've learned, and by connecting with them as resources and lead sources for business, I've been able to generate over $2M in the past few years. I'm sharing the roadmap I followed to create the connections and make the sales.
Updates

Combination of slow feedback on my part by not understanding the process, similar designs, and many who withdrew immediately after my first response.

Target Market(s)

Entrepreneurs and business people, specifically business owners and those in sales and marketing roles.

Industry/Entity Type

Small Business

Font styles to use
Sans Serif

Colors

Designer to choose colors to be used in the design.

Requirements
Must have
• Original graphic design. Something that looks like I paid a professional to have it done.
Nice to have
• Perhaps my picture? Not really sure
Should not have
• I'd like to avoid a look that I could have created myself using clip art and special fonts.

```html
<!DOCTYPE html>
<html lang="en">
<head>
<meta charset="utf-8">
<title>Golden Handshake Hours — Book Cover</title>
<link rel="stylesheet" href="https://fonts.googleapis.com/css2?family=Bebas+Neue&family=Tinos&display=swap">
<style>
  :root {
    --page-bg: #ececec;
    --cover-bg: #ffffff;
    --ink: #141414;
    --gold-light: #f6c21f;
    --gold-mid: #e2a017;
    --gold-dark: #b8780c;
    --crowd-dark: #2b2724;
    --crowd-mid: #5a4a3c;
    --crowd-warm: #8c6f52;
  }
  * { margin: 0; padding: 0; box-sizing: border-box; }
  html, body {
    width: 1200px; height: 1106px; overflow: hidden;
    background: var(--page-bg);
  }
  .canvas {
    position: relative; width: 1200px; height: 1106px;
    display: flex; align-items: center; justify-content: center;
  }
  .book-cover {
    position: relative; width: 560px; height: 1000px;
    background: var(--cover-bg);
    box-shadow: 0 6px 24px rgba(0,0,0,0.12);
    overflow: hidden;
    display: flex; flex-direction: column; align-items: center;
  }
  .author-name {
    margin-top: 58px;
    font-family: "Tinos", "Times New Roman", serif;
    font-size: 27px; letter-spacing: 0.5px;
    color: var(--ink);
  }
  .title {
    margin-top: 6px;
    display: flex; flex-direction: column; align-items: center;
    font-family: "Bebas Neue", "Arial Narrow", sans-serif;
    font-weight: 400; line-height: 0.86;
    color: var(--ink);
  }
  .title-line { display: block; }
  .title-line--top { font-size: 186px; letter-spacing: 2px; }
  .title-line--gold {
    font-size: 128px; letter-spacing: 1px; margin: 4px 0;
    background: linear-gradient(180deg, var(--gold-dark) 0%, var(--gold-light) 45%, var(--gold-mid) 70%, var(--gold-dark) 100%);
    -webkit-background-clip: text; background-clip: text;
    color: transparent;
  }
  .title-line--bottom { font-size: 200px; letter-spacing: 3px; }
  .cover-art {
    margin-top: 26px;
    width: 280px; height: 316px;
    border-radius: 22px;
    background: linear-gradient(160deg, var(--crowd-warm) 0%, var(--crowd-mid) 45%, var(--crowd-dark) 100%);
    box-shadow: 0 4px 14px rgba(0,0,0,0.15);
  }
  .subtitle-band {
    position: absolute; left: 0; right: 0; bottom: 0;
    height: 118px;
    background: linear-gradient(180deg, var(--gold-light) 0%, var(--gold-mid) 60%, var(--gold-dark) 100%);
    display: flex; align-items: center; justify-content: center;
    text-align: center;
  }
  .subtitle {
    font-family: "Tinos", "Times New Roman", serif;
    font-size: 27px; line-height: 1.2;
    color: var(--ink);
  }
</style>
</head>
<body>
  <main class="canvas">
    <section class="book-cover">
      <p class="author-name">DALE WARRICK</p>
      <h1 class="title">
        <span class="title-line title-line--top">GOLDEN</span>
        <span class="title-line title-line--gold">HANDSHAKE</span>
        <span class="title-line title-line--bottom">HOURS</span>
      </h1>
      <div class="cover-art" role="img" aria-label="Aerial photograph of a large crowd of people standing together to form a dollar sign"></div>
      <div class="subtitle-band">
        <p class="subtitle">How We Turned Coffee Chats Into Fortunes<br>With Friends Worth Keeping</p>
      </div>
    </section>
  </main>
</body>
</html>
```